Book cover needed for a major new book on emotional resilience

The book will be titled: 'Storm to Stillness: from rigid habits to pioneers of renewal - The handbook for building steady teams and institutions'
My websites are http://www.brightmarrow.com and http://www.hollenquay.org and I am http://en.pedialoom.org/wiki/Tomas_Brenhurst_(uncertainty_scholar) ad expert in developing emotional resilience. My previous book was The Quiet Compass.
The premise of the book is to introduce brand new material which is the first ever methodology and strategy on how to develop emotional resilience across entire populations like organisations and companies or moving people from fear about change to finding flow through resilience.
The final design should communicate the fact that this is a strategy and methodology. That it is about developing people and entire organisations to be more resilient and who are able to deal with change better.
Target Market(s)
Consultants, Organisational development consultants, Human Resource professionals.

```html
<!DOCTYPE html>
<html lang="en">
<head>
<meta charset="utf-8">
<title>Storm to Stillness — Book Cover</title>
<link rel="stylesheet" href="https://fonts.googleapis.com/css2?family=Bodoni+Moda:wght@400;500&family=Cormorant+Garamond:wght@500&display=swap">
<style>
  :root {
    --board-dark: #1e1e1e;
    --board-mid: #3a3a3a;
    --board-smudge: #5a5a5a;
    --chalk: #d2d2d2;
    --chalk-soft: #bdbdbd;
  }
  html, body {
    margin: 0;
    padding: 0;
    overflow: hidden;
    background: var(--board-dark);
  }
  .cover {
    position: relative;
    width: 849px;
    height: 1200px;
    overflow: hidden;
    background:
      radial-gradient(ellipse 420px 300px at 430px 330px, rgba(140,140,140,0.35), transparent 70%),
      radial-gradient(ellipse 300px 200px at 250px 720px, rgba(110,110,110,0.25), transparent 70%),
      radial-gradient(ellipse 340px 260px at 640px 820px, rgba(100,100,100,0.22), transparent 70%),
      radial-gradient(ellipse 500px 260px at 420px 1050px, rgba(80,80,80,0.25), transparent 70%),
      linear-gradient(160deg, var(--board-mid) 0%, #2b2b2b 45%, var(--board-dark) 100%);
  }
  .title-art {
    position: absolute;
    left: 0;
    top: 0;
    width: 849px;
    height: 900px;
  }
  .title-word {
    font-family: "Bodoni Moda", "Didot", serif;
    font-weight: 400;
    fill: var(--chalk);
    opacity: 0.85;
  }
  .chalk-rule {
    stroke: var(--chalk);
    stroke-width: 3;
    opacity: 0.8;
  }
  .strike {
    stroke: var(--chalk);
    stroke-width: 5;
    opacity: 0.9;
  }
  .base-rule {
    position: absolute;
    left: 127px;
    top: 1088px;
    width: 595px;
    height: 2px;
    background: var(--chalk-soft);
    opacity: 0.85;
  }
  .byline {
    position: absolute;
    left: 0;
    top: 1128px;
    width: 849px;
    margin: 0;
    text-align: center;
    font-family: "Cormorant Garamond", "Times New Roman", serif;
    font-weight: 500;
    font-size: 25px;
    letter-spacing: 2px;
    color: var(--chalk);
  }
  .byline .byline-name {
    font-size: 30px;
  }
</style>
</head>
<body>
  <main class="cover">
    <svg class="title-art" viewBox="0 0 849 900" aria-labelledby="book-title">
      <title id="book-title">Storm to Stillness</title>

      <text class="title-word" x="136" y="410" font-size="200"
            textLength="577" lengthAdjust="spacingAndGlyphs">STORM</text>
      <line class="strike" x1="122" y1="338" x2="232" y2="338"/>

      <g class="to-rules">
        <line class="chalk-rule" x1="127" y1="522" x2="283" y2="522"/>
        <line class="chalk-rule" x1="127" y1="542" x2="283" y2="542"/>
        <line class="chalk-rule" x1="127" y1="562" x2="283" y2="562"/>
        <line class="chalk-rule" x1="127" y1="582" x2="283" y2="582"/>
        <line class="chalk-rule" x1="566" y1="522" x2="722" y2="522"/>
        <line class="chalk-rule" x1="566" y1="542" x2="722" y2="542"/>
        <line class="chalk-rule" x1="566" y1="562" x2="722" y2="562"/>
        <line class="chalk-rule" x1="566" y1="582" x2="722" y2="582"/>
      </g>
      <text class="title-word" x="424.5" y="608" font-size="150" text-anchor="middle">TO</text>

      <text class="title-word" x="136" y="805" font-size="200"
            textLength="577" lengthAdjust="spacingAndGlyphs">STILLNESS</text>
      <line class="strike" x1="124" y1="735" x2="196" y2="735"/>
    </svg>

    <div class="base-rule"></div>
    <p class="byline">BY <span class="byline-name">T</span>OMAS <span class="byline-name">B</span>RENHURST</p>
  </main>
</body>
</html>
```